We need a business card design for a Dubai based company .

We need a business card for a Dubai based company called "Marwaneq Smoking Requisites Trading LLC". We mainly import Flavoured Tobacco products and Charcoal which is used for smoking in a Hookah/Shisha and distribute to the wholesalers and retailers. Logo file is attached herewith.

```html
<!DOCTYPE html>
<html lang="en">
<head>
<meta charset="utf-8">
<title>Marwaneq Smoking Requisites Trading LLC – Business Card</title>
<link rel="stylesheet" href="https://fonts.googleapis.com/css2?family=Roboto+Condensed:wght@300;400;700&display=swap">
<style>
  :root {
    --page-bg: #e9e7e3;
    --card-white: #ffffff;
    --card-dark: #333333;
    --brand-red: #c4242b;
    --ink: #1c1c1c;
    --ink-soft: #555555;
    --silver: #d9d9d9;
  }
  * { box-sizing: border-box; margin: 0; padding: 0; }
  html, body {
    width: 1200px; height: 768px; overflow: hidden;
    background: var(--page-bg);
    font-family: "Roboto Condensed", Arial, sans-serif;
  }
  .stage {
    width: 1200px; height: 768px;
    display: flex; align-items: center; justify-content: center; gap: 40px;
  }
  .card {
    width: 540px; height: 310px; position: relative; overflow: hidden;
    box-shadow: 0 6px 18px rgba(0,0,0,0.18);
  }
  /* Front */
  .card-front { background: var(--card-white); }
  .brand-name {
    font-weight: 400; color: var(--ink); text-align: center;
    text-transform: uppercase; letter-spacing: 0.14em; line-height: 1.15;
  }
  .card-front .brand-name {
    position: absolute; top: 44px; left: 140px; width: 260px;
    font-size: 13px;
  }
  .card-front .brand-name .brand-word { display: block; font-size: 32px; letter-spacing: 0.16em; }
  .holder {
    position: absolute; left: 34px; top: 168px;
  }
  .holder-name {
    font-weight: 700; font-size: 22px; color: var(--ink); text-transform: uppercase;
  }
  .holder-role { font-weight: 300; font-size: 16px; color: var(--brand-red); }
  .divider {
    position: absolute; left: 34px; right: 34px; top: 222px;
    height: 1.5px; background: var(--brand-red);
  }
  .contacts {
    position: absolute; left: 34px; right: 34px; top: 234px;
    display: flex; justify-content: space-between;
    font-size: 13px; font-weight: 300; color: var(--ink-soft); line-height: 1.35;
  }
  .contact-item { display: flex; gap: 6px; align-items: flex-start; }
  .contact-item svg { width: 10px; height: 10px; margin-top: 3px; flex: none; fill: var(--brand-red); }
  .contact-web { color: var(--brand-red); font-weight: 700; }
  .contact-web .tld { font-weight: 700; }
  .bottom-band {
    position: absolute; left: 0; right: 0; bottom: 0; height: 8px;
    background: var(--brand-red);
  }
  /* Back */
  .card-back { background: var(--card-dark); display: flex; align-items: center; justify-content: center; }
  .card-back .brand-name { color: var(--silver); font-size: 15px; }
  .card-back .brand-name .brand-word { display: block; font-size: 52px; letter-spacing: 0.16em; }
</style>
</head>
<body>
<main class="stage">
  <section class="card card-front" aria-label="Business card front">
    <div class="brand-name"><span class="brand-word">Marwaneq</span>Smoking Requisites Trading LLC</div>

    <div class="holder">
      <p class="holder-name">Daniel Hart</p>
      <p class="holder-role">President</p>
    </div>

    <div class="divider"></div>

    <div class="contacts">
      <div class="contact-item">
        <svg viewBox="0 0 10 10" aria-hidden="true"><path d="M5 0a3.6 3.6 0 0 0-3.6 3.6C1.4 6.3 5 10 5 10s3.6-3.7 3.6-6.4A3.6 3.6 0 0 0 5 0zm0 5a1.4 1.4 0 1 1 0-2.8A1.4 1.4 0 0 1 5 5z"/></svg>
        <p>214 Juniper Court<br>Fairbanks, Alaska 99701</p>
      </div>
      <div>
        <div class="contact-item">
          <svg viewBox="0 0 10 10" aria-hidden="true"><path d="M2 0.5l1.6 2.1-0.9 1.1c0.6 1.2 1.5 2.1 2.7 2.7l1.1-0.9 2.1 1.6-0.8 1.9C4.4 8.8 1.2 5.6 0.2 1.2z"/></svg>
          <p>555-014-2237</p>
        </div>
        <div class="contact-item">
          <svg viewBox="0 0 10 10" aria-hidden="true"><path d="M0 2h10v6H0zM0.6 2.4L5 5.6l4.4-3.2"/></svg>
          <p>info@marwaneqsrt.com</p>
        </div>
      </div>
      <div class="contact-item contact-web">
        <svg viewBox="0 0 10 10" aria-hidden="true"><circle cx="5" cy="5" r="4.5"/></svg>
        <p>marwaneqsrt<span class="tld">.com</span></p>
      </div>
    </div>

    <div class="bottom-band"></div>
  </section>

  <section class="card card-back" aria-label="Business card back">
    <div class="brand-name"><span class="brand-word">Marwaneq</span>Smoking Requisites Trading LLC</div>
  </section>
</main>
</body>
</html>
```